Career Counselor in need of a business card design

Hello Creatives! I'm in need of a business card design for a new company based in Georgia, USA called Pathways By Lumen.

Some things that may be helpful in creating your concept(s) include:

My Logo (Included in the Files section): There are three versions, two versions are in the second file. The all gold stacked (vertical) version is my primary logo and then there are two horizontal versions (one is all gold and the other is gold and grey).

My mission: to empower tweens through young adults to realize and actualize their CAREER ASPIRATIONS.
My vision: for tweens through young adults to LIVE LIFE ON PURPOSE and become CONTRIBUTING MEMBERS OF SOCIETY.

Biblical scriptures that support my ‘Why’: Psalms 127: 3-4(NIV) Children are a heritage from the Lord, offspring a reward from him. Like ARROWS in the hands of a warrior are children…. And Proverbs 29:18(JKV) Where there is no VISION, the people perish.

*Words in ALL CAPS are to emphasize what's important to me and may possibly provide you some inspiration (IDK - Have fun with it)!

Target Market(s)

My ideal customers are parents, guardians, and young adults.

Contact Information for Business Card

My name, degrees and credential: Delmira Fosket, M.S., Ed.S., NCC
Title: College and Career Coach and Consultant

Number: 555.317.8842
Address: 2618 Velbrook Avenue., Suite 407, Macon, GA 31299
Email: info@pathwaysbylumen.co
Website: www.pathwaysbylumen.co

My population: TWEENS • TEENS • EMERGING ADULTS
Services offered: One-On-One Sessions • Small Groups • Workshops

Colors

Designer to choose colors to be used in the design.

Requirements
Nice to have
• Either my mission or vision but I will understand if it does not all fit.
• My mission: To empower tweens through young adults to realize and actualize their career aspirations.
• My vision: For tweens through young adults to live life on purpose and become contributing members of society.

```html
<!DOCTYPE html>
<html lang="en">
<head>
<meta charset="utf-8">
<title>Pathways By Lumen — Business Card</title>
<link href="https://fonts.googleapis.com/css2?family=Open+Sans:wght@400;600;700&display=swap" rel="stylesheet">
<style>
  :root {
    --bg: #e9e7e6;
    --card: #1c1c1d;
    --card-edge: #2a2a2b;
    --gold: #d4a72c;
    --gold-soft: #b8912a;
    --white: #f2f2f2;
    --emboss: #2e2e30;
    --font: "Open Sans", Arial, sans-serif;
  }
  * { box-sizing: border-box; margin: 0; padding: 0; }
  html, body { width: 1200px; height: 1200px; overflow: hidden; }
  body {
    background: var(--bg);
    font-family: var(--font);
    display: flex;
    flex-direction: column;
    align-items: center;
    justify-content: center;
    gap: 60px;
  }
  .card {
    width: 900px;
    height: 514px;
    background: var(--card);
    border-radius: 40px;
    position: relative;
    overflow: hidden;
    box-shadow: 0 0 0 1px var(--card-edge);
  }

  /* Back side */
  .card--back {
    display: flex;
    flex-direction: column;
    align-items: center;
    justify-content: center;
  }
  .brand-mark {
    display: flex;
    align-items: center;
    gap: 22px;
  }
  .brand-mark__circle {
    width: 88px; height: 88px;
    border-radius: 50%;
    border: 4px solid currentColor;
  }
  .brand-mark__name {
    font-weight: 600;
    font-size: 52px;
    letter-spacing: 1px;
    line-height: 1;
  }
  .card--back .brand-mark { color: var(--emboss); margin-bottom: 70px; }
  .audience, .services {
    color: var(--gold-soft);
    font-size: 19px;
    letter-spacing: 0.5px;
    text-align: center;
  }
  .services { margin-top: 14px; }

  /* Front side */
  .card--front {
    display: flex;
    align-items: center;
  }
  .front-brand {
    width: 455px;
    display: flex;
    justify-content: center;
    color: var(--gold);
  }
  .front-brand .brand-mark {
    flex-direction: column;
    gap: 20px;
  }
  .front-brand .brand-mark__circle { width: 110px; height: 110px; border-width: 5px; }
  .front-brand .brand-mark__name { font-size: 40px; }
  .divider {
    width: 2px;
    height: 300px;
    background: var(--white);
  }
  .details {
    padding-left: 46px;
    color: var(--white);
  }
  .details__name {
    font-weight: 700;
    font-size: 27px;
    color: var(--gold);
    letter-spacing: 0.3px;
  }
  .details__creds {
    font-weight: 400;
    font-size: 17px;
    color: var(--white);
    margin-left: 4px;
  }
  .details__title { font-size: 18px; margin-top: 4px; }
  .details__address { font-size: 18px; margin-top: 22px; line-height: 1.35; font-style: normal; }
  .contact { list-style: none; margin-top: 22px; font-size: 18px; line-height: 1.5; }
  .contact li { display: flex; align-items: center; gap: 12px; }
  .contact svg { width: 16px; height: 16px; fill: var(--gold); flex: none; }
  .contact .accent { color: var(--gold); }
</style>
</head>
<body>

  <section class="card card--back" aria-label="Business card, back">
    <div class="brand-mark">
      <span class="brand-mark__circle"></span>
      <span class="brand-mark__name">Pathways By Lumen</span>
    </div>
    <p class="audience">TWEENS • TEENS • EMERGING ADULTS</p>
    <p class="services">Services : One-On-One Sessions • Small Groups • Workshops</p>
  </section>

  <section class="card card--front" aria-label="Business card, front">
    <div class="front-brand">
      <div class="brand-mark">
        <span class="brand-mark__circle"></span>
        <span class="brand-mark__name">Pathways By Lumen</span>
      </div>
    </div>
    <div class="divider"></div>
    <div class="details">
      <h1 class="details__name">DELMIRA FOSKET <span class="details__creds">M.S., ED.S., NCC</span></h1>
      <p class="details__title">College &amp; Career Coach &amp; Consultant</p>
      <address class="details__address">2618 Velbrook Avenue<br>Suite 407, Macon, GA 31299</address>
      <ul class="contact">
        <li>
          <svg viewBox="0 0 24 24" aria-hidden="true"><path d="M6.6 10.8a15.1 15.1 0 0 0 6.6 6.6l2.2-2.2a1 1 0 0 1 1-.25 11.4 11.4 0 0 0 3.6.57 1 1 0 0 1 1 1V20a1 1 0 0 1-1 1A17 17 0 0 1 3 4a1 1 0 0 1 1-1h3.5a1 1 0 0 1 1 1c0 1.25.2 2.45.57 3.57a1 1 0 0 1-.25 1z"/></svg>
          555-317-8842
        </li>
        <li>
          <svg viewBox="0 0 24 24" aria-hidden="true"><path d="M2 5h20v14H2z M4 7v.5l8 5 8-5V7l-8 5z" fill-rule="evenodd"/></svg>
          info@pathwaysbylumen.co
        </li>
        <li>
          <svg viewBox="0 0 24 24" aria-hidden="true"><circle cx="12" cy="12" r="9"/></svg>
          <span>www.<span class="accent">pathwaysbylumen</span>.co</span>
        </li>
      </ul>
    </div>
  </section>

</body>
</html>
```